Brightmere Holdings - Business Cards

We would need to design our Company Business Cards for the following People:

1. Thomas Pirelli
Director/Licensee-In-Charge
M: 0412 579 304
T: (02) 7314 2296
E: thomas@brightmere.com.au
Website: www.brightmereholdings.com

2. Marcus Holt
Project Manager
M: 0421 367 915
T: (02) 7314 2296
E: marcus@brightmereholdings.com

3. Priya Ravindrasekar
Property Officer
M: 0477 218 643
T: (02) 7314 2296
E: priya@brightmereholdings.com

Address: Level 9, 27 Harbour Lane W, Parramatta NSW 2150
The above address is the SAME for ALL Cards.

This Card is to be Double-Sided.
Front - With the above Information & Details.
Back - Showing the Services:
Property Services, Financial Solutions, Special Projects.

ALL Office Locations:
Sydney: (02) 7314 2296
Melbourne: (03) 9241 5503
Brisbane: (07) 3466 1982
Malaysia (JB): (+601) 7293 6048
Singapore: (+65) 9182 4637

We intend on making a Design/Template for the Business Card & duplicating these Business Cards for the above 3x People.
Please USE & REFER to the above FULL Name, Job Title, Mobile, Office Phone, Email & Website.

```html
<!DOCTYPE html>
<html lang="en">
<head>
<meta charset="utf-8">
<title>Brightmere Holdings – Business Cards</title>
<link rel="stylesheet" href="https://fonts.googleapis.com/css2?family=Work+Sans:wght@400;500;600&display=swap">
<style>
  :root {
    --stage: #161616;
    --card: #222223;
    --card-light: #2b2b2c;
    --ink: #f2f2f2;
    --accent: #e3e31c;
  }
  * { box-sizing: border-box; margin: 0; padding: 0; }
  html, body { width: 1200px; height: 900px; overflow: hidden; }
  body {
    background: var(--stage);
    font-family: "Work Sans", sans-serif;
    color: var(--ink);
    position: relative;
  }
  .card {
    position: absolute;
    left: 250px;
    width: 700px;
    height: 400px;
    background: linear-gradient(135deg, var(--card) 0%, var(--card-light) 70%, var(--card) 100%);
    box-shadow: 0 10px 30px rgba(0,0,0,.55);
  }
  .card--back { top: 35px; }
  .card--front { top: 465px; }

  .brand {
    display: flex;
    align-items: center;
    gap: 14px;
    position: absolute;
  }
  .brand__mark {
    width: 14px; height: 14px;
    flex: none;
    background: var(--accent);
  }
  .brand__name {
    font-weight: 400;
    color: var(--ink);
    text-transform: uppercase;
    white-space: nowrap;
  }
  .card--back .brand { left: 0; right: 0; top: 150px; justify-content: center; }
  .card--back .brand__name { font-size: 34px; letter-spacing: 9px; }

  .services {
    position: absolute;
    left: 0; right: 0; bottom: 60px;
    text-align: center;
    font-size: 17px;
    font-weight: 500;
    letter-spacing: 1px;
  }
  .services .divider { color: var(--accent); margin: 0 6px; }

  .card--front .brand { left: 40px; top: 180px; gap: 12px; }
  .card--front .brand__mark { width: 12px; height: 12px; }
  .card--front .brand__name { font-size: 16px; letter-spacing: 3px; }

  .rule {
    position: absolute;
    left: 372px; top: 55px;
    width: 2px; height: 250px;
    background: var(--accent);
  }
  .contact {
    position: absolute;
    left: 398px; top: 55px;
    width: 290px;
  }
  .contact__name {
    font-size: 26px;
    font-weight: 600;
    color: var(--accent);
    letter-spacing: 1.5px;
    text-transform: uppercase;
  }
  .contact__role { font-size: 16px; letter-spacing: .8px; margin-top: 2px; }
  .contact__address { font-size: 15px; letter-spacing: .6px; line-height: 1.35; margin-top: 14px; }
  .contact__list { list-style: none; margin-top: 14px; font-size: 15px; letter-spacing: .6px; line-height: 1.55; }
  .contact__list li { display: flex; align-items: center; gap: 10px; white-space: nowrap; }
  .contact__list svg { width: 12px; height: 12px; flex: none; stroke: var(--accent); fill: none; stroke-width: 1.5; }
  .contact__list .domain { color: var(--accent); }
</style>
</head>
<body>
  <section class="card card--back">
    <div class="brand">
      <span class="brand__mark"></span>
      <span class="brand__name">Brightmere Holdings</span>
    </div>
    <p class="services">Property Services<span class="divider">|</span>Financial Solutions<span class="divider">|</span>Special Projects.</p>
  </section>

  <section class="card card--front">
    <div class="brand">
      <span class="brand__mark"></span>
      <span class="brand__name">Brightmere Holdings</span>
    </div>
    <div class="rule"></div>
    <div class="contact">
      <h1 class="contact__name">Marcus Holt</h1>
      <p class="contact__role">Project Manager</p>
      <p class="contact__address">Level 9, 27 Harbour Lane W,<br>Parramatta NSW 2150</p>
      <ul class="contact__list">
        <li><svg viewBox="0 0 12 12"><path d="M2 1.5l2 0 1 2.5-1.3 1a6 6 0 0 0 3.3 3.3l1-1.3 2.5 1v2a1 1 0 0 1-1 1A9 9 0 0 1 1 2.5a1 1 0 0 1 1-1z"/></svg><span>0421 367 915</span></li>
        <li><svg viewBox="0 0 12 12"><rect x="3" y="1" width="6" height="10" rx="1"/><path d="M5.5 9h1"/></svg><span>(02) 7314 2296</span></li>
        <li><svg viewBox="0 0 12 12"><rect x="1" y="2.5" width="10" height="7"/><path d="M1 2.5l5 4 5-4"/></svg><span>marcus@brightmereholdings.com</span></li>
        <li><svg viewBox="0 0 12 12"><circle cx="6" cy="6" r="5"/><path d="M1 6h10M6 1c-3 3-3 7 0 10M6 1c3 3 3 7 0 10"/></svg><span>www.<span class="domain">brightmereholdings</span>.com</span></li>
      </ul>
    </div>
  </section>
</body>
</html>
```